Business Card design for a company called Tallow Flame NI

I need a business card design for my oil fired boiler servicing company. I have a logo design already and Im just looking that incorporated into the business card design. card details; Tallow Flame NI
Oil Burner Servicing - Mid Ulster Area
Service Engineer - Owen Marsh
Mobile 07751364927
email - Tallow.Flame.NI@hearthmail.example
www.tallowflameni.example
I carry out Servicing, Commissioning, Fault Finding, Warranty Validation
Target Market(s)
home owners with oil fired central heating
Industry/Entity Type
Business
Contact Information for Business Card
Tallow Flame NI
Tell. 07751364927
Web: www.tallowflameni.example
email Tallow.Flame.NI@Hearthmail.Example
Servicing Fault Finding Commissioning Warranty Validation
Look and feel

```html
<!DOCTYPE html>
<html lang="en">
<head>
<meta charset="utf-8">
<title>Tallow Flame NI – Business Card</title>
<link href="https://fonts.googleapis.com/css2?family=Open+Sans:wght@300;400;600;700&display=swap" rel="stylesheet">
<style>
  :root{
    --green:#5cbf3a;
    --green-light:#9ad43c;
    --green-dark:#3f9e2b;
    --grey:#9a9c98;
    --ink:#3b3b3b;
    --paper:#ffffff;
    --charcoal:#303030;
    --backdrop:#e9e9e6;
    --muted:#dcdcdc;
  }
  *{box-sizing:border-box;margin:0;padding:0}
  html,body{width:1200px;height:950px;overflow:hidden}
  body{
    background:var(--backdrop);
    font-family:"Open Sans",Arial,sans-serif;
    color:var(--ink);
    display:flex;flex-direction:column;align-items:center;justify-content:center;gap:32px;
  }
  .card{
    width:760px;height:434px;position:relative;overflow:hidden;
    box-shadow:0 6px 18px rgba(0,0,0,.18);
  }

  /* Front */
  .card--front{
    background:linear-gradient(200deg,#eef6e2 0%,var(--paper) 38%);
  }
  .brand{position:absolute;left:64px;top:104px;display:flex;align-items:center;gap:16px}
  .brand__dot{width:58px;height:58px;border-radius:50%;background:var(--green)}
  .brand__name{font-weight:700;font-size:46px;color:var(--green);line-height:1;letter-spacing:-.5px}
  .brand__tagline{
    position:absolute;left:140px;top:160px;font-size:11px;font-weight:600;
    letter-spacing:2px;text-transform:uppercase;color:var(--green-dark)
  }
  .person{position:absolute;left:64px;top:262px}
  .person__name{font-size:26px;font-weight:400;color:var(--green);line-height:1.2}
  .person__role{font-size:18px;color:var(--ink)}
  .contact{
    position:absolute;top:236px;display:flex;flex-direction:column;gap:10px;
    padding-left:18px;border-left:1px solid var(--muted);height:96px;
  }
  .contact--phone{left:262px}
  .contact--web{left:434px}
  .contact__row{display:flex;align-items:center;gap:8px;font-size:17px;line-height:26px;color:var(--ink);white-space:nowrap}
  .contact--web .contact__row{font-size:14px}
  .contact__icon{width:16px;height:20px;flex:none}
  .card__band{
    position:absolute;left:0;right:0;bottom:0;height:22px;
    background:linear-gradient(90deg,var(--green) 0%,var(--green-light) 62%,var(--grey) 62%,var(--grey) 100%);
  }

  /* Back */
  .card--back{background:var(--charcoal);color:#fff}
  .back__brand{position:absolute;left:64px;top:232px;display:flex;align-items:center;gap:14px}
  .back__dot{width:40px;height:40px;border-radius:50%;background:var(--green)}
  .back__name{font-weight:700;font-size:40px;color:var(--green);line-height:1}
  .back__tagline{
    position:absolute;left:118px;top:280px;font-size:10px;font-weight:600;
    letter-spacing:2px;text-transform:uppercase;color:var(--green)
  }
  .services{position:absolute;left:64px;top:316px;list-style:none;font-size:20px;font-weight:300;line-height:1.45;color:#f1f1f1}
</style>
</head>
<body>

  <article class="card card--front">
    <div class="brand">
      <span class="brand__dot"></span>
      <span class="brand__name">Tallow Flame NI</span>
    </div>
    <p class="brand__tagline">Oil Burner Servicing · Mid Ulster Area</p>

    <div class="person">
      <p class="person__name">Owen Marsh</p>
      <p class="person__role">Service Engineer</p>
    </div>

    <div class="contact contact--phone">
      <p class="contact__row">
        <svg class="contact__icon" viewBox="0 0 16 20"><rect x="2" y="1" width="12" height="18" rx="2" fill="none" stroke="#5cbf3a" stroke-width="2"/><circle cx="8" cy="15.5" r="1.3" fill="#5cbf3a"/></svg>
        07751364927
      </p>
      <p class="contact__row">
        <svg class="contact__icon" viewBox="0 0 16 20"><path d="M4 2 L7 6 L5.5 8 Q7 12 10 14 L12 12.5 L15 16 L12.5 18.5 Q4 16 1.5 5 Z" fill="#5cbf3a"/></svg>
        07751364927
      </p>
    </div>

    <div class="contact contact--web">
      <p class="contact__row">Tallow.Flame.NI@hearthmail.example</p>
      <p class="contact__row">www.tallowflameni.example</p>
    </div>

    <div class="card__band"></div>
  </article>

  <article class="card card--back">
    <div class="back__brand">
      <span class="back__dot"></span>
      <span class="back__name">Tallow Flame NI</span>
    </div>
    <p class="back__tagline">Oil Burner Servicing · Mid Ulster Area</p>
    <ul class="services">
      <li>Commissioning Fault Finding</li>
      <li>Warranty Validation</li>
    </ul>
  </article>

</body>
</html>
```